Business Card Design Project

Company Name - Kestrova Care

Wellness consulting and training company. Run through a medical centre.

Main colour themes are orange and blue, as in the logo. Want to replicate same effect with business cards.

To give a sense of freedom and potential as per the company name.

Want the business card to be in line with stationary design, which I have launched as well.

Double sided with design and colour on one side and details on other side.
Updates

Reason: Need business card and stationary design to be teed up.

Target Market(s)

35 to 65 age group.
New age and trendy

Industry/Entity Type

Training

Requirements
Must have
• Colours orange and blue as per logo
Nice to have
• Design to be similar to stationary design, letterhead and envelopes

```html
<!DOCTYPE html>
<html lang="en">
<head>
<meta charset="utf-8">
<title>Kestrova Care — Business Card</title>
<link rel="stylesheet" href="https://fonts.googleapis.com/css2?family=Parisienne&family=Arimo:wght@700&family=Oswald:wght@400&display=swap">
<style>
  :root {
    --ink-blue: #1f5fa3;
    --deep-blue: #2563a0;
    --warm-orange: #e06a2c;
    --soft-peach: #f2c7ae;
    --mist-blue: #a9c4de;
    --paper: #ffffff;
  }
  * { box-sizing: border-box; margin: 0; padding: 0; }
  html, body {
    width: 1048px;
    height: 1200px;
    overflow: hidden;
    background: var(--paper);
  }
  .canvas {
    position: relative;
    width: 1048px;
    height: 1200px;
    background: var(--paper);
  }
  .details-side {
    position: absolute;
    inset: 0 0 600px 0;
  }
  .company-title {
    position: absolute;
    top: 238px;
    left: 0;
    width: 1048px;
    text-align: center;
    font-family: "Parisienne", cursive;
    font-size: 92px;
    font-weight: 400;
    color: var(--ink-blue);
    letter-spacing: 1px;
  }
  .contact-list {
    position: absolute;
    top: 446px;
    left: 50px;
    list-style: none;
  }
  .contact-item {
    display: flex;
    align-items: center;
    height: 24.5px;
    font-family: "Arimo", Arial, sans-serif;
    font-weight: 700;
    font-size: 18.5px;
    color: var(--ink-blue);
  }
  .contact-icon {
    width: 28px;
    height: 22px;
    margin-right: 20px;
    flex: none;
  }
  .brand-side {
    position: absolute;
    left: 0;
    top: 600px;
    width: 1048px;
    height: 600px;
    border-radius: 92px;
    overflow: hidden;
    background:
      radial-gradient(ellipse 300px 260px at 525px 235px, rgba(255,255,255,1) 0%, rgba(255,255,255,0.85) 40%, rgba(255,255,255,0) 100%),
      linear-gradient(90deg, var(--warm-orange) 0%, #e9946a 22%, var(--soft-peach) 38%, #f6ebe6 50%, #d8e3ef 58%, var(--mist-blue) 68%, #6e9ac7 84%, var(--deep-blue) 100%);
  }
  .brand-name {
    position: absolute;
    top: 275px;
    left: 0;
    width: 1048px;
    text-align: center;
    font-family: "Oswald", "Arial Narrow", sans-serif;
    font-weight: 400;
    font-size: 98px;
    line-height: 1;
    color: var(--deep-blue);
  }
</style>
</head>
<body>
<main class="canvas">
  <section class="details-side">
    <h1 class="company-title">Kestrova Care</h1>
    <ul class="contact-list">
      <li class="contact-item">
        <svg class="contact-icon" viewBox="0 0 28 22" aria-hidden="true">
          <circle cx="14" cy="11" r="10" fill="none" stroke="var(--ink-blue)" stroke-width="1.6"/>
          <path d="M9 15c2-5 5-8 10-9l1 2c-4 1-6 3-8 8z" fill="var(--ink-blue)"/>
        </svg>
        <span>Phone:(000) 000-0000</span>
      </li>
      <li class="contact-item">
        <svg class="contact-icon" viewBox="0 0 28 22" aria-hidden="true">
          <rect x="2" y="5" width="24" height="13" fill="none" stroke="var(--ink-blue)" stroke-width="1.6"/>
          <line x1="5" y1="10" x2="23" y2="10" stroke="var(--ink-blue)" stroke-width="1.4"/>
          <line x1="5" y1="14" x2="18" y2="14" stroke="var(--ink-blue)" stroke-width="1.4"/>
        </svg>
        <span>&nbsp;Fax&nbsp;&nbsp;&nbsp;&nbsp;&nbsp;:(000) 000-0000</span>
      </li>
      <li class="contact-item">
        <svg class="contact-icon" viewBox="0 0 28 22" aria-hidden="true">
          <path d="M3 4h9c1 0 2 1 2 2v13c0-1-1-2-2-2H3z M25 4h-9c-1 0-2 1-2 2v13c0-1 1-2 2-2h9z" fill="none" stroke="var(--ink-blue)" stroke-width="1.6"/>
        </svg>
        <span>Address:City, State and Zip</span>
      </li>
      <li class="contact-item">
        <svg class="contact-icon" viewBox="0 0 28 22" aria-hidden="true">
          <rect x="6" y="3" width="16" height="12" fill="none" stroke="var(--ink-blue)" stroke-width="1.6"/>
          <rect x="4" y="17" width="20" height="3" fill="var(--ink-blue)"/>
        </svg>
        <span>E-mail:www.kestrovacare.com</span>
      </li>
    </ul>
  </section>

  <section class="brand-side">
    <p class="brand-name">Kestrova Care</p>
  </section>
</main>
</body>
</html>
```